KRV In Home Flier

To prepare a flier to be placed directly into existing clients homes, which shares additional services available. These are clients that are using KRV Cleaning Services and we want to use our KRV Pest Control or BMO (Bravo Mend On)Maintenance Services

Target Market(s)

residential home owners / Renters

Industry/Entity Type

Property Maintenance

Colors

Designer to choose colors to be used in the design.

Requirements
Must have
• Must be crisp and clean - design should pop - A CLEAR call to action
Nice to have
• See previous designed uploaded
Should not have

```html
<!DOCTYPE html>
<html lang="en">
<head>
<meta charset="utf-8">
<title>KRV In Home Flier</title>
<link rel="stylesheet" href="https://fonts.googleapis.com/css2?family=Oswald:wght@400;500&family=Open+Sans:wght@400;600&display=swap">
<style>
  :root {
    --page-bg: #e6e6e4;
    --white: #ffffff;
    --blue: #0a6fb8;
    --blue-dark: #0b4f8a;
    --orange: #f7941d;
    --red: #b3262d;
    --ink: #2b2b2b;
    --grey-text: #555555;
    --partner: #4a3a86;
    --photo-pest-a: #c9ced3;
    --photo-pest-b: #8e969c;
    --photo-home-a: #d9dde0;
    --photo-home-b: #5d7486;
  }
  * { box-sizing: border-box; margin: 0; padding: 0; }
  html, body { width: 1200px; height: 838px; overflow: hidden; background: var(--page-bg); }
  .canvas { position: relative; width: 1200px; height: 838px; }

  .flier {
    position: absolute; top: 54px; width: 519px; height: 734px;
    background: var(--white); overflow: hidden;
    box-shadow: 0 4px 14px rgba(0,0,0,.25);
    font-family: "Open Sans", Arial, sans-serif;
  }
  .flier--pest { left: 61px; --accent: var(--orange); }
  .flier--home { left: 620px; --accent: var(--red); }

  .hero { position: absolute; left: 0; top: 0; width: 519px; height: 400px; }

  .title-tag {
    position: absolute; left: 0; top: 0; height: 43px; width: 280px;
    background: var(--accent);
    clip-path: polygon(0 0, 100% 0, calc(100% - 16px) 100%, 0 100%);
    color: var(--white); font-family: "Oswald", Arial, sans-serif; font-weight: 500;
    font-size: 25px; line-height: 43px; padding-left: 22px;
  }
  .tagline {
    position: absolute; left: 20px; top: 188px; color: var(--white);
    font-family: "Oswald", Arial, sans-serif; font-weight: 500; font-size: 20px;
    letter-spacing: -0.2px; text-shadow: 0 1px 3px rgba(0,0,0,.45);
  }

  .section-title {
    position: absolute; left: 20px; top: 398px; color: var(--blue);
    font-family: "Oswald", Arial, sans-serif; font-weight: 500; font-size: 21px;
  }

  .service-list { position: absolute; left: 20px; list-style: none; }
  .service {
    position: absolute; left: 0; display: flex; align-items: center; gap: 12px;
    white-space: nowrap; color: var(--ink);
    font-family: "Oswald", Arial, sans-serif; font-weight: 500; font-size: 18px;
  }
  .service svg { width: 38px; height: 38px; flex: none; }

  .brand-name {
    position: absolute; color: var(--blue); font-size: 20px; font-weight: 600;
    display: flex; align-items: center; gap: 8px; white-space: nowrap;
  }
  .brand-name .mark { width: 14px; height: 14px; border-radius: 50%; background: var(--blue); }

  .feature-list { position: absolute; left: 272px; top: 496px; list-style: none; }
  .feature-list li {
    position: relative; padding-left: 18px; color: var(--grey-text);
    font-size: 12px; font-weight: 600; line-height: 15px; margin-bottom: 6px;
  }
  .feature-list svg { position: absolute; left: 0; top: 2px; width: 12px; height: 10px; }

  .about {
    position: absolute; left: 275px; top: 495px; width: 235px; color: var(--grey-text);
    font-size: 14.5px; line-height: 24px;
  }

  .partner {
    position: absolute; left: 270px; top: 610px; width: 125px; color: var(--partner);
    font-size: 14px; font-weight: 600; line-height: 16px;
    display: flex; align-items: center; gap: 7px;
  }
  .partner .mark { width: 12px; height: 12px; background: var(--partner); flex: none; }

  .offer-badge { position: absolute; left: 404px; top: 553px; width: 108px; height: 108px; }

  .cta-bar { position: absolute; left: 0; bottom: 0; width: 519px; height: 63px; }
  .cta-bar svg { position: absolute; inset: 0; }
  .cta-text {
    position: absolute; left: 20px; top: 17px; color: var(--white); white-space: nowrap;
    font-family: "Oswald", Arial, sans-serif; font-size: 19px; letter-spacing: -0.2px;
  }
  .cta-phone {
    position: absolute; right: 22px; top: 4px; text-align: right; color: var(--white);
    font-family: "Oswald", Arial, sans-serif; line-height: 1; white-space: nowrap;
  }
  .cta-phone .number { display: block; font-size: 28px; font-weight: 500; }
  .cta-phone .digits { display: block; font-size: 17px; margin-top: 2px; }
</style>
</head>
<body>
<main class="canvas">

  <section class="flier flier--pest">
    <svg class="hero" viewBox="0 0 519 400">
      <defs>
        <linearGradient id="pestPhoto" x1="0" y1="0" x2="1" y2="1">
          <stop offset="0" stop-color="var(--photo-pest-a)"/>
          <stop offset="1" stop-color="var(--photo-pest-b)"/>
        </linearGradient>
      </defs>
      <polygon role="img" aria-label="Photo of a technician in a white protective suit holding a pest spray tank" points="0,0 519,0 519,262 259,375 0,262" fill="url(#pestPhoto)"/>
      <polygon points="0,262 259,375 519,262 519,278 259,391 0,278" fill="var(--blue)"/>
    </svg>
    <div class="title-tag">PEST CONTROL SERVICE</div>
    <p class="tagline">YOUR PROPERTY, OUR PRIORITY.</p>

    <h2 class="section-title">OUR SERVICES</h2>
    <ul class="service-list">
      <li class="service" style="top:438px"><svg viewBox="0 0 40 40"><circle cx="20" cy="20" r="17" fill="none" stroke="var(--orange)" stroke-width="4"/><rect x="15" y="11" width="10" height="18" rx="2" fill="var(--ink)"/></svg>GENERAL PEST CONTROL</li>
      <li class="service" style="top:480px"><svg viewBox="0 0 40 40"><circle cx="20" cy="20" r="17" fill="none" stroke="var(--orange)" stroke-width="4"/><ellipse cx="20" cy="20" rx="6" ry="8" fill="var(--ink)"/><line x1="8" y1="8" x2="32" y2="32" stroke="var(--orange)" stroke-width="4"/></svg>BED BUGS CONTROL</li>
      <li class="service" style="top:522px"><svg viewBox="0 0 40 40"><circle cx="20" cy="20" r="17" fill="none" stroke="var(--orange)" stroke-width="4"/><ellipse cx="20" cy="21" rx="9" ry="6" fill="var(--ink)"/><line x1="8" y1="8" x2="32" y2="32" stroke="var(--orange)" stroke-width="4"/></svg>RAT CONTROL</li>
      <li class="service" style="top:563px"><svg viewBox="0 0 40 40"><circle cx="20" cy="20" r="17" fill="none" stroke="var(--orange)" stroke-width="4"/><ellipse cx="20" cy="20" rx="5" ry="9" fill="var(--ink)"/><line x1="8" y1="8" x2="32" y2="32" stroke="var(--orange)" stroke-width="4"/></svg>COCKROACHES CONTROL</li>
      <li class="service" style="top:605px"><svg viewBox="0 0 40 40"><circle cx="20" cy="20" r="17" fill="none" stroke="var(--orange)" stroke-width="4"/><circle cx="20" cy="15" r="3" fill="var(--ink)"/><circle cx="20" cy="23" r="4" fill="var(--ink)"/><line x1="8" y1="8" x2="32" y2="32" stroke="var(--orange)" stroke-width="4"/></svg>ANT CONTROL</li>
    </ul>

    <div class="brand-name" style="left:272px; top:440px"><span class="mark"></span>KRV Pest Control</div>

    <ul class="feature-list">
      <li><svg viewBox="0 0 12 10"><polyline points="1,5 4.5,8.5 11,1" fill="none" stroke="var(--orange)" stroke-width="1.8"/></svg>EUROPEAN MANAGED</li>
      <li><svg viewBox="0 0 12 10"><polyline points="1,5 4.5,8.5 11,1" fill="none" stroke="var(--orange)" stroke-width="1.8"/></svg>MONTHLY - QUARTERLY - ANNUALLY<br>MAINTENANCE CONTRACTS</li>
      <li><svg viewBox="0 0 12 10"><polyline points="1,5 4.5,8.5 11,1" fill="none" stroke="var(--orange)" stroke-width="1.8"/></svg>ON CALL SERVICE</li>
    </ul>

    <div class="partner"><span class="mark"></span><span>KRV Cleaning<br>Services</span></div>

    <svg class="offer-badge" viewBox="0 0 110 110">
      <circle cx="55" cy="55" r="53" fill="var(--blue)" stroke="var(--blue-dark)" stroke-width="3" stroke-dasharray="6 3"/>
      <circle cx="55" cy="55" r="46" fill="var(--blue)"/>
      <text x="55" y="52" text-anchor="middle" fill="#fff" font-family="Oswald, sans-serif" font-size="34">10%</text>
      <text x="55" y="70" text-anchor="middle" fill="#fff" font-family="Open Sans, sans-serif" font-weight="600" font-size="11">FOR OUR</text>
      <text x="55" y="85" text-anchor="middle" fill="#fff" font-family="Open Sans, sans-serif" font-weight="600" font-size="11">KRV CLIENTS</text>
    </svg>

    <div class="cta-bar">
      <svg viewBox="0 0 519 63" preserveAspectRatio="none">
        <rect width="519" height="63" fill="var(--orange)"/>
        <polygon points="0,0 330,0 312,63 0,63" fill="var(--blue)"/>
        <polygon points="330,0 338,0 320,63 312,63" fill="var(--white)"/>
      </svg>
      <p class="cta-text">CALL US NOW FOR A FREE ESTIMATE!</p>
      <p class="cta-phone"><span class="number">800 HOMEFIX</span><span class="digits">(46 63 34 9)</span></p>
    </div>
  </section>

  <section class="flier flier--home">
    <svg class="hero" viewBox="0 0 519 400">
      <defs>
        <linearGradient id="homePhoto" x1="0" y1="0" x2="1" y2="1">
          <stop offset="0" stop-color="var(--photo-home-a)"/>
          <stop offset="1" stop-color="var(--photo-home-b)"/>
        </linearGradient>
      </defs>
      <polygon role="img" aria-label="Photo of a handyman with a yellow hard hat and tool belt in a kitchen" points="0,0 519,0 519,262 259,375 0,262" fill="url(#homePhoto)"/>
      <polygon points="0,262 259,375 519,262 519,278 259,391 0,278" fill="var(--blue)"/>
    </svg>
    <div class="title-tag">HOME MAINTENANCE</div>
    <p class="tagline">YOUR PROPERTY, OUR PRIORITY.</p>

    <h2 class="section-title">OUR SERVICES</h2>
    <ul class="service-list">
      <li class="service" style="top:450px"><svg viewBox="0 0 40 40"><circle cx="20" cy="20" r="18" fill="var(--red)"/><g stroke="#fff" stroke-width="2"><line x1="20" y1="10" x2="20" y2="30"/><line x1="10" y1="20" x2="30" y2="20"/><line x1="13" y1="13" x2="27" y2="27"/><line x1="27" y1="13" x2="13" y2="27"/></g></svg>AC SERVICES</li>
      <li class="service" style="top:501px"><svg viewBox="0 0 40 40"><circle cx="20" cy="20" r="18" fill="var(--red)"/><path d="M11 17h12v10h-4v-6h-8z" fill="#fff"/></svg>PLUMBING SERVICES</li>
      <li class="service" style="top:551px"><svg viewBox="0 0 40 40"><circle cx="20" cy="20" r="18" fill="var(--red)"/><circle cx="20" cy="18" r="6" fill="none" stroke="#fff" stroke-width="2"/><rect x="17" y="25" width="6" height="4" fill="#fff"/></svg>ELECTRICAL SERVICES</li>
      <li class="service" style="top:602px"><svg viewBox="0 0 40 40"><circle cx="20" cy="20" r="18" fill="var(--red)"/><g stroke="#fff" stroke-width="3" stroke-linecap="round"><line x1="12" y1="12" x2="28" y2="28"/><line x1="28" y1="12" x2="12" y2="28"/></g></svg>HANDYMAN SERVICES</li>
    </ul>

    <div class="brand-name" style="left:284px; top:455px"><span class="mark"></span>Bravo Mend On</div>

    <p class="about">FOCUS ON QUALITY &amp; SERVICING CLIENTS NEEDS 24 HOURS A DAY 365 DAYS A YEAR.</p>

    <div class="partner"><span class="mark"></span><span>KRV Cleaning<br>Services</span></div>

    <svg class="offer-badge" viewBox="0 0 110 110">
      <circle cx="55" cy="55" r="53" fill="var(--blue)" stroke="var(--blue-dark)" stroke-width="3" stroke-dasharray="6 3"/>
      <circle cx="55" cy="55" r="46" fill="var(--blue)"/>
      <text x="55" y="52" text-anchor="middle" fill="#fff" font-family="Oswald, sans-serif" font-size="34">10%</text>
      <text x="55" y="70" text-anchor="middle" fill="#fff" font-family="Open Sans, sans-serif" font-weight="600" font-size="11">FOR OUR</text>
      <text x="55" y="85" text-anchor="middle" fill="#fff" font-family="Open Sans, sans-serif" font-weight="600" font-size="11">KRV CLIENTS</text>
    </svg>

    <div class="cta-bar">
      <svg viewBox="0 0 519 63" preserveAspectRatio="none">
        <rect width="519" height="63" fill="var(--red)"/>
        <polygon points="0,0 330,0 312,63 0,63" fill="var(--blue)"/>
        <polygon points="330,0 338,0 320,63 312,63" fill="var(--white)"/>
      </svg>
      <p class="cta-text">CALL US NOW FOR A FREE ESTIMATE!</p>
      <p class="cta-phone"><span class="number">800 HOMEFIX</span><span class="digits">(46 63 34 9)</span></p>
    </div>
  </section>

</main>
</body>
</html>
```